Breezeway Comfort business cards design

Need a business card design for a Heating and Air Conditioning business. I need these items included.
Business name: Breezeway Comfort
Owner: Marcus Tollefsen
License # 2874590
Phone number # 555-382-4071
Email: breezewaycomfortair@mailvista.example
Sales
Service
Installation
Maintenance

Heating and Air Conditioning

Requirements
Must have
• Company name , license number , phone number , email

```html
<!DOCTYPE html>
<html lang="en">
<head>
<meta charset="utf-8">
<title>Breezeway Comfort – Business Cards</title>
<link rel="stylesheet" href="https://fonts.googleapis.com/css2?family=Roboto+Condensed:wght@400;700&display=swap">
<style>
  :root {
    --bg: #e4e5e7;
    --card: #ffffff;
    --blue: #1c3f9e;
    --orange: #f48a2c;
    --coral: #f2603a;
    --pink: #e8306a;
    --text-grey: #4a4a4a;
    --rule: #f07aa0;
    --faint-warm: #fbe3d6;
    --faint-cool: #e6ebf6;
  }
  * { box-sizing: border-box; margin: 0; padding: 0; }
  html, body { width: 1200px; height: 800px; overflow: hidden; }
  body {
    background: var(--bg);
    font-family: "Roboto Condensed", "Arial Narrow", sans-serif;
    position: relative;
  }
  .card {
    position: absolute;
    top: 251px;
    width: 520px;
    height: 298px;
    background: var(--card);
    border-radius: 3px;
    box-shadow: 0 6px 18px rgba(0,0,0,0.12);
    overflow: hidden;
  }
  .card--front { left: 50px; }
  .card--back { left: 630px; }

  .card__bands { position: absolute; inset: 0; width: 100%; height: 100%; }

  .decor-area {
    position: absolute;
    border-radius: 50%;
    background: radial-gradient(circle at 45% 40%, var(--faint-warm) 0%, rgba(251,227,214,0.5) 40%, var(--faint-cool) 65%, rgba(255,255,255,0) 75%);
    opacity: 0.8;
  }
  .card--front .decor-area { left: 40px; top: -20px; width: 230px; height: 230px; }
  .card--back .decor-area { left: 110px; top: -20px; width: 230px; height: 230px; }

  .brand { position: absolute; right: 24px; text-align: left; }
  .brand__name {
    display: flex; align-items: center; gap: 7px;
    color: var(--blue);
    font-weight: 700;
    font-size: 26px;
    line-height: 1;
    text-transform: uppercase;
    white-space: nowrap;
  }
  .brand__dot {
    width: 13px; height: 13px; border-radius: 50%;
    background: var(--orange);
    flex: none;
  }
  .brand__tagline {
    margin-top: 6px;
    color: var(--orange);
    font-weight: 700;
    font-size: 16px;
    letter-spacing: 4px;
    text-transform: uppercase;
    border-top: 1px solid var(--blue);
    padding-top: 5px;
    white-space: nowrap;
  }
  .card--front .brand { top: 146px; }
  .card--back .brand { top: 128px; }
  .card--back .brand__name { font-size: 24px; }
  .card--back .brand__tagline { font-size: 15px; letter-spacing: 3px; }

  .services {
    margin-top: 6px;
    color: var(--pink);
    font-size: 15px;
    border-top: 1px solid var(--blue);
    padding-top: 4px;
    white-space: nowrap;
  }

  .contact { position: absolute; left: 36px; top: 36px; width: 340px; }
  .contact__name {
    color: var(--blue);
    font-weight: 700;
    font-size: 16px;
    text-transform: uppercase;
  }
  .contact__role { color: var(--text-grey); font-weight: 400; text-transform: none; }
  .contact__rule { height: 1px; background: var(--rule); margin: 8px 0; }
  .contact__line {
    display: flex; align-items: center; gap: 5px;
    color: var(--text-grey);
    font-size: 13px;
    white-space: nowrap;
  }
  .contact__line svg { width: 12px; height: 12px; flex: none; }
  .contact__sep { margin: 0 3px; }

  .license {
    position: absolute;
    right: 22px; bottom: 22px;
    color: #ffffff;
    font-size: 15px;
  }
</style>
</head>
<body>

  <section class="card card--front" aria-label="Business card front">
    <div class="decor-area" role="img" aria-label="Faint brand decoration area in soft warm and cool tones"></div>
    <svg class="card__bands" viewBox="0 0 520 298" preserveAspectRatio="none" aria-hidden="true">
      <defs>
        <linearGradient id="frontTab" x1="0" y1="0" x2="1" y2="1">
          <stop offset="0" stop-color="#e8306a"/>
          <stop offset="1" stop-color="#f26a3a"/>
        </linearGradient>
        <linearGradient id="frontBand" x1="0" y1="0" x2="1" y2="0">
          <stop offset="0" stop-color="#f2603a"/>
          <stop offset="1" stop-color="#f7953a"/>
        </linearGradient>
      </defs>
      <path d="M0 190 H128 Q140 190 140 202 V232 H0 Z" fill="url(#frontTab)"/>
      <path d="M146 244 H520 V298 H166 Z" fill="url(#frontBand)"/>
    </svg>
    <div class="brand">
      <div class="brand__name"><span class="brand__dot"></span>Breezeway Comfort</div>
      <div class="brand__tagline">Heating &amp; Air</div>
      <div class="services">Sales | Service | Installation | Maintenance</div>
    </div>
  </section>

  <section class="card card--back" aria-label="Business card back">
    <div class="decor-area" role="img" aria-label="Faint brand decoration area in soft warm and cool tones"></div>
    <svg class="card__bands" viewBox="0 0 520 298" preserveAspectRatio="none" aria-hidden="true">
      <defs>
        <linearGradient id="backBand" x1="0" y1="0" x2="1" y2="0">
          <stop offset="0" stop-color="#f7953a"/>
          <stop offset="1" stop-color="#f2603a"/>
        </linearGradient>
        <linearGradient id="backTab" x1="0" y1="0" x2="1" y2="0">
          <stop offset="0" stop-color="#f2603a"/>
          <stop offset="1" stop-color="#e8306a"/>
        </linearGradient>
      </defs>
      <path d="M0 172 H250 L234 240 H0 Z" fill="url(#backBand)"/>
      <path d="M324 248 Q330 234 346 234 H520 V298 H310 Z" fill="url(#backTab)"/>
    </svg>
    <div class="contact">
      <div class="contact__name">Marcus Tollefsen <span class="contact__role">| Owner</span></div>
      <div class="contact__rule"></div>
      <div class="contact__line">
        <svg viewBox="0 0 24 24" aria-hidden="true"><path fill="#1c3f9e" d="M6.6 10.8a15 15 0 0 0 6.6 6.6l2.2-2.2a1 1 0 0 1 1-.25 11.4 11.4 0 0 0 3.6.57 1 1 0 0 1 1 1V20a1 1 0 0 1-1 1A17 17 0 0 1 3 4a1 1 0 0 1 1-1h3.5a1 1 0 0 1 1 1c0 1.25.2 2.45.57 3.57a1 1 0 0 1-.25 1z"/></svg>
        555-382-4071<span class="contact__sep">|</span>
        <svg viewBox="0 0 24 24" aria-hidden="true"><path fill="#1c3f9e" d="M2 5h20v14H2z M4 7v.4l8 5 8-5V7l-8 5z" fill-rule="evenodd"/></svg>
        breezewaycomfortair@mailvista.example
      </div>
      <div class="contact__rule"></div>
    </div>
    <div class="brand">
      <div class="brand__name"><span class="brand__dot"></span>Breezeway Comfort</div>
      <div class="brand__tagline">Heating &amp; Air</div>
    </div>
    <div class="license">License # 2874590</div>
  </section>

</body>
</html>
```